Willowmere Recovery Brochure

We need a brochure template we can change photo's and words at a later date. WE offer rehabilitation to injured horses and ponies.
Either use our Willowmere Grounds or Willowmere Recovery logo but not both. A strong preference for the horse being led to feature first.

Target Market(s)

Horse Owners

Font styles to use
Serif

Colors
f78f20

Requirements
Must have
• Ability to write the text and interchange photos within the layout at a later date.
Nice to have
• Our colours are orange and black

```html
<!DOCTYPE html>
<html lang="en">
<head>
<meta charset="utf-8">
<title>Willowmere Recovery Brochure</title>
<link href="https://fonts.googleapis.com/css2?family=Cinzel:wght@400;700&family=Great+Vibes&family=Open+Sans:wght@400;600&display=swap" rel="stylesheet">
<style>
  :root {
    --orange: #f78f20;
    --orange-deep: #e9822a;
    --white: #ffffff;
    --ink: #1c1c1c;
    --backdrop: #eeeeee;
    --photo-brown: #8a5a3a;
    --photo-green: #6f7d4e;
    --photo-blue: #5c7f92;
    --photo-grey: #8c8c88;
  }
  html, body { margin: 0; padding: 0; overflow: hidden; }
  body { background: var(--backdrop); }
  .canvas {
    position: relative; width: 904px; height: 1200px; overflow: hidden;
    background: var(--backdrop);
    font-family: "Open Sans", Arial, sans-serif; color: var(--white);
  }
  .sheet {
    position: absolute; left: 22px; width: 860px; height: 550px;
    display: grid; grid-template-columns: repeat(3, 1fr);
    background: var(--orange);
    box-shadow: 0 6px 18px rgba(0,0,0,.18);
  }
  .sheet--outside { top: 30px; }
  .sheet--inside { top: 620px; }
  .panel { position: relative; overflow: hidden; }
  .panel + .panel { border-left: 1px solid rgba(0,0,0,.08); }
  .heading {
    font-family: "Cinzel", Georgia, serif; font-weight: 700; font-size: 15px;
    letter-spacing: .5px; text-transform: uppercase; text-align: center;
    margin: 0 auto 12px; padding-bottom: 6px; width: max-content;
    border-bottom: 1px solid rgba(255,255,255,.8);
  }
  .body-text { font-size: 11.5px; line-height: 1.45; text-align: center; margin: 0 0 12px; }
  .photo { position: absolute; }

  /* Outside: mission panel */
  .mission { padding: 30px 26px 0; }
  .mission .photo {
    left: 0; top: 205px; width: 258px; height: 320px;
    border-radius: 0 70px 90px 0;
    background: linear-gradient(160deg, var(--photo-grey), var(--photo-brown) 55%, #3e3a36);
  }

  /* Outside: contact panel */
  .contact { padding: 120px 24px 0; }
  .contact-list { list-style: none; margin: 18px 0 0; padding: 0; }
  .contact-item { display: flex; align-items: center; gap: 14px; margin-bottom: 22px; font-size: 12.5px; line-height: 1.35; }
  .contact-item--phone { font-size: 17px; }
  .contact-icon { flex: none; width: 32px; height: 32px; }

  /* Outside: cover panel */
  .cover-top { position: absolute; inset: 0 0 auto 0; height: 250px; }
  .brand {
    position: absolute; top: 88px; left: 0; right: 0; text-align: center;
    font-family: "Cinzel", Georgia, serif; font-weight: 400; font-size: 22px;
    color: var(--orange); line-height: 1.15;
  }
  .cover .photo {
    left: 18px; right: 0; top: 270px; bottom: 0;
    border-radius: 60px 0 0 0;
    background: linear-gradient(150deg, var(--photo-green), var(--photo-brown) 50%, #4a4640);
  }
  .tagline {
    position: absolute; left: 40px; right: 14px; top: 395px;
    font-family: "Cinzel", Georgia, serif; text-align: center; text-transform: uppercase;
    text-shadow: 0 1px 3px rgba(0,0,0,.4);
  }
  .tagline-small { font-size: 11px; letter-spacing: 4px; display: block; }
  .tagline-big { font-size: 38px; font-weight: 700; line-height: 1; display: block; }
  .tagline-mid { font-size: 11px; letter-spacing: 2px; display: block; border-top: 1px solid #fff; border-bottom: 1px solid #fff; width: 70%; margin: 3px auto; }
  .tagline-end { font-size: 17px; font-weight: 700; display: block; }

  /* Inside: care panel */
  .care .photo { left: 0; right: 0; top: 0; height: 185px;
    background: linear-gradient(90deg, #6a3b2a, var(--photo-brown) 50%, #a06842); }
  .care-title { position: absolute; top: 200px; left: 0; right: 0; text-align: center; font-family: "Cinzel", Georgia, serif; }
  .care-kicker { font-size: 15px; letter-spacing: 5px; display: block; }
  .care-script { font-family: "Great Vibes", cursive; font-size: 56px; line-height: .9; display: block; }
  .care-end { font-size: 19px; font-weight: 700; display: block; }
  .about { position: absolute; top: 330px; left: 24px; right: 24px; }

  /* Inside: gallery panel */
  .gallery .photo { left: 0; right: 0; }
  .photo--pool { top: 0; height: 175px; background: linear-gradient(180deg, #b79a80, var(--photo-blue) 70%, #3f6f7e); }
  .photo--handler { top: 175px; height: 195px; background: linear-gradient(135deg, #6c6a68, #4a3426 60%, #2c2622); }
  .photo--treadmill { top: 370px; height: 180px; background: linear-gradient(180deg, #d9d5cf, #6e6a64 60%, #2d2b29); }

  /* Inside: services panel */
  .services { padding: 24px 22px 0; }
  .services .heading { margin-left: 0; text-align: left; }
  .service-list { list-style: none; margin: 6px 0 0; padding: 0; font-size: 15px; line-height: 1.55; }
  .service-list li { display: flex; align-items: flex-start; gap: 10px; }
  .service-list svg { flex: none; width: 12px; height: 12px; margin-top: 6px; }
  .services .photo { left: 0; right: 0; top: 350px; bottom: 0;
    border-radius: 70px 0 0 0;
    background: linear-gradient(120deg, #c9b28a, #a86a3c 55%, #7a4a2c); }
</style>
</head>
<body>
<div class="canvas">

  <section class="sheet sheet--outside">
    <div class="panel mission">
      <h2 class="heading">Our Mission</h2>
      <p class="body-text">Lorem ipsum dolor Lorem ipsum dolor sit amet, consectetuer adipiscing elit, sed diam nonummy nibh euismod tincidunt ut laoreet consectetuer adipiscing elit, sed diam nonummy nibh euismod tincidunt ut laoreet</p>
      <div class="photo" role="img" aria-label="Chestnut horse standing in an aqua treadmill stall"></div>
    </div>

    <div class="panel contact">
      <h2 class="heading">Contact Us</h2>
      <ul class="contact-list">
        <li class="contact-item contact-item--phone">
          <svg class="contact-icon" viewBox="0 0 32 32" fill="none" stroke="#fff" stroke-width="1.5"><circle cx="16" cy="16" r="14"/><path d="M12 9l3 3-2 2c1 2 3 4 5 5l2-2 3 3-2 2c-5 0-11-6-11-11z"/></svg>
          303-555-0148
        </li>
        <li class="contact-item">
          <svg class="contact-icon" viewBox="0 0 32 32" fill="none" stroke="#fff" stroke-width="1.5"><circle cx="16" cy="16" r="14"/><path d="M16 24s-6-6-6-10a6 6 0 0 1 12 0c0 4-6 10-6 10z"/><circle cx="16" cy="14" r="2"/></svg>
          <span>1180 Larkspur Lane<br>Fort Collins, CO 80521</span>
        </li>
        <li class="contact-item">
          <svg class="contact-icon" viewBox="0 0 32 32" fill="none" stroke="#fff" stroke-width="1.5"><circle cx="16" cy="16" r="14"/><rect x="9" y="11" width="14" height="10"/><path d="M9 11l7 6 7-6"/></svg>
          <span>info@willowmere<br>recovery.com</span>
        </li>
      </ul>
    </div>

    <div class="panel cover">
      <svg class="cover-top" viewBox="0 0 287 250" preserveAspectRatio="none"><path d="M0 0H287V205C240 215 200 240 150 240C95 240 70 200 55 150C40 100 20 40 0 0Z" fill="#fff"/></svg>
      <div class="brand">Willowmere<br>Recovery</div>
      <div class="photo" role="img" aria-label="Handler leading a chestnut horse along a tree-lined path"></div>
      <p class="tagline">
        <span class="tagline-small">We help in giving</span>
        <span class="tagline-big">Life Back</span>
        <span class="tagline-mid">to your</span>
        <span class="tagline-end">Horses and Ponies.</span>
      </p>
    </div>
  </section>

  <section class="sheet sheet--inside">
    <div class="panel care">
      <div class="photo" role="img" aria-label="Horse leg wound before and after treatment"></div>
      <h2 class="care-title">
        <span class="care-kicker">Remarkable</span>
        <span class="care-script">Care</span>
        <span class="care-end">and Treatment</span>
      </h2>
      <div class="about">
        <h3 class="heading">About Us</h3>
        <p class="body-text">Lorem ipsum dolor Lorem ipsum dolor sit amet, consectetuer adipiscing elit, sed diam nonummy nibh euismod tincidunt ut laoreet consectetuer adipiscing elit, sed diam nonummy nibh euismod tincidunt ut laoreet</p>
        <p class="body-text">sed diam nonummy nibh euismod tincidunt ut laoreet consectetuer adipiscing elit, sed diam nonummy nibh euismod tincidunt ut laoreet</p>
      </div>
    </div>

    <div class="panel gallery">
      <div class="photo photo--pool" role="img" aria-label="Horse swimming in a therapy pool"></div>
      <div class="photo photo--handler" role="img" aria-label="Therapist working on a horse's head and neck"></div>
      <div class="photo photo--treadmill" role="img" aria-label="Horse on an indoor water treadmill with staff"></div>
    </div>

    <div class="panel services">
      <h2 class="heading">Rehabilitation<br>Services</h2>
      <ul class="service-list">
        <li><svg viewBox="0 0 12 12" fill="none" stroke="#fff" stroke-width="1.5"><path d="M2 6l3 3 5-6"/></svg>Water Walker</li>
        <li><svg viewBox="0 0 12 12" fill="none" stroke="#fff" stroke-width="1.5"><path d="M2 6l3 3 5-6"/></svg>Free Swimming Pool</li>
        <li><svg viewBox="0 0 12 12" fill="none" stroke="#fff" stroke-width="1.5"><path d="M2 6l3 3 5-6"/></svg>Cold Salt Chambers</li>
        <li><svg viewBox="0 0 12 12" fill="none" stroke="#fff" stroke-width="1.5"><path d="M2 6l3 3 5-6"/></svg>Pulseplate/solarium</li>
        <li><svg viewBox="0 0 12 12" fill="none" stroke="#fff" stroke-width="1.5"><path d="M2 6l3 3 5-6"/></svg>Cold Laser Therapy</li>
        <li><svg viewBox="0 0 12 12" fill="none" stroke="#fff" stroke-width="1.5"><path d="M2 6l3 3 5-6"/></svg>EQ-ultrasound</li>
        <li><svg viewBox="0 0 12 12" fill="none" stroke="#fff" stroke-width="1.5"><path d="M2 6l3 3 5-6"/></svg>AERO-RESP</li>
        <li><svg viewBox="0 0 12 12" fill="none" stroke="#fff" stroke-width="1.5"><path d="M2 6l3 3 5-6"/></svg>Equine Chiropractic<br>&amp; Massage</li>
      </ul>
      <div class="photo" role="img" aria-label="Owner in a straw hat embracing a chestnut horse outdoors"></div>
    </div>
  </section>

</div>
</body>
</html>
```